KL Taxidermy

I need business Cards with my logo and a background photo of one of my taxidermy mounts.
I would like a black back drop behind it all and what ever looks best for my contact information (red or white?)
Garrick Pembley
592-718-4409
kltaxidermy482@mailnook.example
Chatterloom page

```html
<!DOCTYPE html>
<html lang="en">
<head>
<meta charset="utf-8">
<title>KL Taxidermy – Business Card</title>
<link rel="stylesheet" href="https://fonts.googleapis.com/css2?family=Lato:wght@400;700&display=swap">
<style>
  :root {
    --stage: #e9e6e1;
    --card-top: #3a3d3f;
    --card-bottom: #1f2123;
    --ink-light: #f2f2f0;
    --accent-copper: #c98a5e;
    --mount-light: #e6e4df;
    --mount-mid: #b9b6b0;
    --rock: #5d6268;
  }
  html, body {
    margin: 0;
    width: 1200px;
    height: 894px;
    overflow: hidden;
    background: var(--stage);
    font-family: "Lato", "Helvetica Neue", Arial, sans-serif;
  }
  .stage {
    width: 1200px;
    height: 894px;
    display: flex;
    align-items: center;
    justify-content: center;
  }
  .business-card {
    position: relative;
    width: 1050px;
    height: 600px;
    background: linear-gradient(160deg, var(--card-top) 0%, var(--card-bottom) 100%);
    box-shadow: 0 18px 40px rgba(0,0,0,0.25);
    overflow: hidden;
    color: var(--ink-light);
  }
  .brand {
    position: absolute;
    left: 70px;
    top: 70px;
    display: flex;
    align-items: center;
    gap: 14px;
  }
  .brand-mark {
    width: 22px;
    height: 22px;
    border-radius: 50%;
    background: var(--ink-light);
  }
  .brand-name {
    font-size: 30px;
    font-weight: 700;
    letter-spacing: 2px;
    text-transform: uppercase;
    color: var(--ink-light);
  }
  .contact-list {
    position: absolute;
    left: 70px;
    top: 250px;
    margin: 0;
    padding: 0;
    list-style: none;
  }
  .contact-item {
    display: flex;
    align-items: center;
    gap: 16px;
    font-size: 21px;
    line-height: 1;
    margin-bottom: 18px;
    white-space: nowrap;
  }
  .contact-icon {
    width: 18px;
    height: 18px;
    flex: none;
  }
  .mount-photo {
    position: absolute;
    left: 460px;
    top: 190px;
    width: 310px;
    height: 410px;
    border-radius: 46% 40% 0 0 / 34% 28% 0 0;
    background:
      radial-gradient(ellipse at 62% 42%, var(--mount-light) 0%, var(--mount-mid) 48%, rgba(185,182,176,0) 78%),
      radial-gradient(ellipse at 22% 78%, var(--rock) 0%, rgba(93,98,104,0) 62%);
  }
  .identity {
    position: absolute;
    left: 790px;
    top: 300px;
  }
  .person-name {
    margin: 0;
    font-size: 30px;
    font-weight: 700;
    color: var(--accent-copper);
    white-space: nowrap;
  }
  .person-role {
    margin: 6px 0 0;
    font-size: 23px;
    font-weight: 400;
    color: var(--ink-light);
  }
</style>
</head>
<body>
<main class="stage">
  <article class="business-card">
    <header class="brand">
      <span class="brand-mark"></span>
      <span class="brand-name">KL Taxidermy</span>
    </header>

    <ul class="contact-list">
      <li class="contact-item">
        <svg class="contact-icon" viewBox="0 0 20 20" aria-hidden="true">
          <path d="M5 2 L8 2 L9 6 L7 8 Q9 12 12 13 L14 11 L18 12 L18 15 Q18 18 15 18 Q3 17 2 5 Q2 2 5 2 Z" fill="var(--accent-copper)"/>
        </svg>
        <span>592-718-4409</span>
      </li>
      <li class="contact-item">
        <svg class="contact-icon" viewBox="0 0 20 20" aria-hidden="true">
          <rect x="1" y="4" width="18" height="12" fill="var(--accent-copper)"/>
          <path d="M1 4 L10 11 L19 4" fill="none" stroke="var(--card-bottom)" stroke-width="1.6"/>
        </svg>
        <span>kltaxidermy482@mailnook.example</span>
      </li>
      <li class="contact-item">
        <svg class="contact-icon" viewBox="0 0 20 20" aria-hidden="true">
          <rect x="1" y="1" width="18" height="18" fill="var(--accent-copper)"/>
        </svg>
        <span>/KLTAXIDERMY</span>
      </li>
    </ul>

    <div class="mount-photo" role="img" aria-label="Photo of a white Dall sheep ram taxidermy mount resting on a grey rock"></div>

    <div class="identity">
      <h1 class="person-name">Garrick Pembley</h1>
      <p class="person-role">Taxidermist</p>
    </div>
  </article>
</main>
</body>
</html>
```